Business Card Design

Hello Designer,
This is an internet based company. We specialize in low rate advertisement space on a number of our websites, Similar to roamjournal. We also Do keyword seo, social media development and management, website development,and mobile friendly reformatting of websites. The overall design should communicate Brightlane Links provides customers with easy access to our advertised businesses, to connect businesses to their desired customers and vice versa.
Updates

Hello Designers!,

If you would like to view my website for ideas please visit. sarasotaventro.example
Also I would like the "BRIGHTLANE LINKS" lettering to be different colors, like Zentros lettering. Also the color scheme I was thinking was blue, white, black
Thank you for taking on this project,
CorinĀ 

Industry/Entity Type

Internet

Contact Information for Business Card

Brightlane Links,Corin Mossfeld,CEO, corin@ventrowww.example, CELL: 941-555-0162, 4182 Larkspur Ln Sarasota 34231,corin@ventrowww.example, Making The Internet More Affordable and Manageable,sarasotaventro.example
ON BACK: Making The Internet More Affordable and Manageable, sarasotaventro,tampaventro,miamiventro,pensacolaventro,jacksonvilleventro, and more, many more.

```html
<!DOCTYPE html>
<html lang="en">
<head>
<meta charset="utf-8">
<title>Brightlane Links – Business Card</title>
<link rel="stylesheet" href="https://fonts.googleapis.com/css2?family=Questrial&family=Oswald:wght@600&display=swap">
<style>
  :root {
    --stage: #c9c9c9;
    --card-white: #ffffff;
    --card-dark: #15181c;
    --card-dark-edge: #0b0d10;
    --accent-blue: #2aa0d8;
    --band-blue: #3f63b8;
    --band-ink: #0d1620;
    --logo-navy: #123a6b;
    --text-light: #f2f4f6;
  }
  * { box-sizing: border-box; margin: 0; padding: 0; }
  html, body {
    width: 1200px; height: 900px; overflow: hidden;
    background: var(--stage);
    font-family: "Questrial", sans-serif;
  }
  .stage {
    position: relative; width: 1200px; height: 900px;
    display: flex; align-items: center; justify-content: center; gap: 50px;
  }
  .card {
    position: relative; width: 540px; height: 310px;
    border-radius: 26px; overflow: hidden;
    background: radial-gradient(ellipse at 60% 40%, #1f2329 0%, var(--card-dark) 55%, var(--card-dark-edge) 100%);
  }

  /* Front */
  .card-front__top {
    height: 128px; background: var(--card-white);
    display: flex; align-items: center; padding-left: 44px; gap: 16px;
  }
  .logotype {
    color: var(--logo-navy); font-family: "Questrial", sans-serif;
    line-height: 1.05;
  }
  .logotype__name { font-size: 34px; letter-spacing: 1px; }
  .logotype__url { font-size: 22px; }
  .logotype__mark {
    width: 74px; height: 74px; border-radius: 50%;
    background: var(--accent-blue); flex: none;
  }
  .tagline-band {
    height: 16px; background: var(--band-blue);
    font-family: "Oswald", sans-serif; font-weight: 600;
    font-size: 11.5px; letter-spacing: 3.6px; line-height: 16px;
    color: var(--band-ink); padding-left: 22px; white-space: nowrap;
  }
  .card-front__body { padding: 10px 26px; }
  .person__name { color: var(--accent-blue); font-size: 17px; }
  .person__role { color: var(--text-light); font-size: 11px; margin-top: 1px; }
  .contact-list { list-style: none; margin-top: 18px; }
  .contact-list li {
    display: flex; align-items: center; gap: 6px;
    color: var(--text-light); font-size: 15px; line-height: 19px;
  }
  .contact-list svg { width: 13px; height: 13px; flex: none; fill: var(--accent-blue); }

  /* Back */
  .card-back {
    display: flex; flex-direction: column; align-items: center;
    padding-top: 62px; color: var(--accent-blue); text-align: center;
  }
  .card-back__tagline { font-size: 17px; margin-bottom: 10px; }
  .site-list { list-style: none; }
  .site-list li { font-size: 17px; line-height: 28.5px; }
</style>
</head>
<body>
<main class="stage">
  <section class="card card-front" aria-label="Card front">
    <div class="card-front__top">
      <div class="logotype">
        <div class="logotype__name">BRIGHTLANE LINKS</div>
        <div class="logotype__url">sarasotaventro.example</div>
      </div>
      <div class="logotype__mark" aria-hidden="true"></div>
    </div>
    <div class="tagline-band">MAKING THE INTERNET MORE AFFORDABLE AND MANAGEABLE</div>
    <div class="card-front__body">
      <div class="person__name">Corin Mossfeld</div>
      <div class="person__role">CEO</div>
      <ul class="contact-list">
        <li><svg viewBox="0 0 16 16"><rect x="4" y="1" width="8" height="14" rx="1.5"/><rect x="5.5" y="3" width="5" height="8" fill="#15181c"/></svg>941-555-0162,</li>
        <li><svg viewBox="0 0 16 16"><rect x="1" y="3" width="14" height="10" rx="1"/><path d="M1.5 3.5 8 9l6.5-5.5" stroke="#15181c" stroke-width="1.4" fill="none"/></svg>corin@ventrowww.example</li>
        <li><svg viewBox="0 0 16 16"><circle cx="8" cy="8" r="7"/><path d="M1 8h14M8 1c-3 3.5-3 10.5 0 14M8 1c3 3.5 3 10.5 0 14" stroke="#15181c" stroke-width="1" fill="none"/></svg>sarasotaventro.example</li>
        <li><svg viewBox="0 0 16 16"><path d="M8 1 1 8h2v7h4v-4h2v4h4V8h2z"/></svg>4182 Larkspur Ln Sarasota 34231</li>
      </ul>
    </div>
  </section>

  <section class="card card-back" aria-label="Card back">
    <p class="card-back__tagline">Making The Internet More Affordable and Manageable</p>
    <ul class="site-list">
      <li>sarasotaventro</li>
      <li>tampaventro</li>
      <li>miamiventro</li>
      <li>pensacolaventro</li>
      <li>jacksonvilleventro</li>
      <li>and more, many more</li>
    </ul>
  </section>
</main>
</body>
</html>
```